Patent Law

Need to develop a home page for a patent lawyer.

Colors should go with logo, blues...

Company Name- Velric Dunmore, PLLC

Company Overview-

I am an Intellectual Property Lawyer and focus on patents, copyrights, trademarks, & trade secrets. I work with small businesses and start ups in the chemical and biotech industries.

Why Us-

I am small firm that can provide large-firm service at a reasonable price. I also can charge flat-fees for entreprenuers in certain practice areas.

Services-
Intellectual Property
Patents
Copyrights
Trademarks
Trade secrets
Healthcare Compliance
Elder law
Wills
Trusts

Website we like-
http://www.tolvanecrest.com/ - within industry!!
http://www.quarnhollet.com/
http://brevicktallon.com/
http://thegravelwrights.com/

Target Market(s)

My customers will be small business, specifically small start-up companies in the chemical and biotech arena.

Industry/Entity Type

Trade

Requirements
Must have
• Colors should go with logo, blues...

```html
<!DOCTYPE html>
<html lang="en">
<head>
<meta charset="utf-8">
<title>Velric Dunmore, PLLC — Intellectual Property Law</title>
<link href="https://fonts.googleapis.com/css2?family=Alegreya+Sans:ital,wght@0,400;0,500;0,700;1,400&family=Roboto+Condensed:wght@700&display=swap" rel="stylesheet">
<style>
:root{
  --brand-blue:#0a8ad8;
  --brand-deep:#0a5fb8;
  --navy:#1f2566;
  --ink:#1d1d2b;
  --text:#222;
  --grey-head:#4a4a4a;
  --panel:#f5f5f5;
  --frame:#e6e6e6;
  --rule:#cfcfcf;
}
*{box-sizing:border-box;margin:0;padding:0}
html,body{width:1200px;height:1000px;overflow:hidden;background:#fff}
body{position:relative;font-family:"Alegreya Sans",sans-serif;color:var(--text)}
a{color:inherit;text-decoration:none}

.top-strip{position:absolute;left:0;top:0;width:1200px;height:7px;background:var(--brand-blue)}
.site-header{position:absolute;left:0;top:7px;width:1200px;height:108px;background:#fff;box-shadow:0 3px 5px rgba(0,0,0,.25)}
.brand{position:absolute;left:157px;top:52px;display:flex;align-items:center;gap:8px;font-weight:500;font-size:17px;letter-spacing:.5px;color:var(--grey-head);text-transform:uppercase}
.brand-dot{width:14px;height:14px;border-radius:50%;background:var(--brand-deep)}
.call{position:absolute;right:183px;top:24px;font-weight:700;font-size:22px;color:var(--grey-head)}
.call span{color:var(--brand-blue)}
.main-nav{position:absolute;left:512px;top:63px;width:514px;height:36px;border-top:2px dotted #888;border-bottom:2px dotted #888;background:linear-gradient(#fff,#eaf4fc 60%,#fff);display:flex;justify-content:flex-end;align-items:center;gap:22px;padding-right:38px;font-size:13px;font-weight:500;color:var(--ink);text-transform:uppercase}
.main-nav .current{color:var(--navy)}

.slider{position:absolute;left:176px;top:134px;width:849px;height:356px;border-radius:10px;background:linear-gradient(#fafafa,var(--frame));border:1px solid #cfcfcf;box-shadow:0 10px 10px -6px rgba(0,0,0,.35)}
.slide-photo{position:absolute;left:13px;top:13px;width:823px;height:327px;border-radius:6px;background:linear-gradient(110deg,#cfd6e2 0%,#a9afb6 30%,#d9d2cb 55%,#ece4dc 75%,#bfc3c8 100%)}
.slide-title{position:absolute;left:66px;top:180px;font-family:"Roboto Condensed",sans-serif;font-weight:700;font-size:37px;line-height:45px;color:var(--ink);text-shadow:0 0 6px #fff,0 0 3px #fff}
.slide-arrow{position:absolute;top:145px;width:60px;height:60px;border-radius:50%;background:#f2f2f2;border:1px solid #d0d0d0;display:flex;align-items:center;justify-content:center}
.slide-arrow.prev{left:-18px}
.slide-arrow.next{right:-18px}
.slide-arrow i{width:38px;height:38px;border-radius:50%;background:linear-gradient(#fff,#cfcfcf);border:1px solid #bbb;display:flex;align-items:center;justify-content:center}

.features{position:absolute;left:175px;top:516px;width:847px;height:318px;background:var(--panel);border-radius:6px;display:flex;box-shadow:0 10px 10px -8px rgba(0,0,0,.2)}
.feature{position:relative;flex:1;height:100%}
.feature + .feature{border-left:2px solid #dcdcdc}
.ribbon{position:absolute;left:68px;top:14px;width:152px;height:62px}
.ribbon-label{position:absolute;top:26px;color:#fff;font-weight:700;font-size:14.5px;line-height:18px;white-space:nowrap;text-transform:uppercase}
.label-why{left:128px}
.label-what{left:120px}
.label-contact{left:125px}
.feature p{position:absolute;left:27px;top:96px;width:234px;font-style:italic;font-size:12.5px;line-height:20.6px}
.feature p + p{top:198px}
.services{position:absolute;left:50px;top:101px;display:grid;grid-template-columns:126px 100px;font-style:italic;font-size:12.5px;line-height:13px}
.services ul{list-style:none}
.services li{position:relative;padding-left:18px;margin-bottom:9.5px}
.services ul:first-child li{width:96px}
.services li::before{content:"";position:absolute;left:0;top:3px;border-left:7px solid #111;border-top:4px solid transparent;border-bottom:4px solid transparent}
.contact-text{position:absolute;left:42px;top:96px;width:232px;font-style:italic;font-size:12.5px;line-height:20.6px}

.site-footer{position:absolute;left:0;top:860px;width:1200px;height:140px;background:linear-gradient(#0a85d6,#1d2a78 75%,#1f2566)}
.footer-map{position:absolute;left:168px;top:20px;width:219px;height:102px;border-radius:30px;background:#c9ced8;opacity:.9}
.footer-nav{position:absolute;left:452px;top:91px;display:flex;gap:19px;font-size:10px;color:#fff;text-transform:uppercase}
.copyright{position:absolute;left:0;width:1230px;top:107px;text-align:center;font-size:9.5px;color:#fff}
.footer-brand{position:absolute;left:862px;top:84px;display:flex;align-items:center;gap:7px;color:#fff;font-size:17px;font-weight:500;text-transform:uppercase;letter-spacing:.5px}
.footer-brand .brand-dot{background:#fff}
</style>
</head>
<body>
<div class="top-strip"></div>
<header class="site-header">
  <div class="brand"><span class="brand-dot"></span>Velric Dunmore, PLLC</div>
  <div class="call">CALL US : <span>444-555-019</span></div>
  <nav class="main-nav">
    <a class="current" href="#">Home</a><a href="#">About</a><a href="#">Practices</a><a href="#">People</a><a href="#">Blogs</a><a href="#">News</a><a href="#">Contact</a>
  </nav>
</header>

<section class="slider">
  <div class="slide-photo" role="img" aria-label="Photo of a lawyer meeting with a smiling young couple"></div>
  <h1 class="slide-title">Connecting<br>Communities, Clients,<br>and People...</h1>
  <div class="slide-arrow prev"><i><svg width="20" height="14" viewBox="0 0 20 14"><path d="M8 1 2 7l6 6V9h10V5H8z" fill="#999"/></svg></i></div>
  <div class="slide-arrow next"><i><svg width="20" height="14" viewBox="0 0 20 14"><path d="M12 1l6 6-6 6V9H2V5h10z" fill="#999"/></svg></i></div>
</section>

<section class="features">
  <article class="feature">
    <svg class="ribbon" viewBox="0 0 152 62"><defs><linearGradient id="rb1" x1="0" y1="0" x2="0" y2="1"><stop offset="0" stop-color="#1a3fa5"/><stop offset="1" stop-color="#0a8ad8"/></linearGradient></defs><path d="M0 0h152v62L76 46 0 62z" fill="#0a8ad8"/><path d="M4 0h144v54L76 40 4 54z" fill="url(#rb1)"/><path d="M16 12v22l5-5 4 8 3-1-4-8h7z" fill="#fff"/><path d="M31 11a6 6 0 1 1 8 5v3" stroke="#fff" stroke-width="3" fill="none"/><circle cx="39" cy="24" r="2" fill="#fff"/></svg>
    <span class="ribbon-label label-why">Why Us</span>
    <p>I am an Intellectual Property Lawyer and focus on patents, copyrights, trademarks, &amp; trade secrets. I work with small businesses and start ups in the chemical and biotech industries.</p>
    <p>I am small firm that can provide large-firm service at a reasonable price. I also can charge flat-fees for entrepreners in certain practice areas.</p>
  </article>
  <article class="feature">
    <svg class="ribbon" viewBox="0 0 152 62"><defs><linearGradient id="rb2" x1="0" y1="0" x2="0" y2="1"><stop offset="0" stop-color="#1a3fa5"/><stop offset="1" stop-color="#0a8ad8"/></linearGradient></defs><path d="M0 0h152v62L76 46 0 62z" fill="#0a8ad8"/><path d="M4 0h144v54L76 40 4 54z" fill="url(#rb2)"/><g stroke="#fff" stroke-width="2" fill="none"><circle cx="17" cy="10" r="3"/><circle cx="17" cy="20" r="3"/><circle cx="17" cy="30" r="3"/><path d="M24 10h17M24 20h17M24 30h17"/></g></svg>
    <span class="ribbon-label label-what">What We Do</span>
    <div class="services">
      <ul><li>Intellectual Property</li><li>Copyrights</li><li>Trade secrets</li><li>Elder law</li><li>Trusts</li></ul>
      <ul><li>Patents</li><li>Trademarks</li><li style="width:80px">Healthcare Compliance</li><li style="margin-top:14px">Wills</li></ul>
    </div>
  </article>
  <article class="feature">
    <svg class="ribbon" viewBox="0 0 152 62"><defs><linearGradient id="rb3" x1="0" y1="0" x2="0" y2="1"><stop offset="0" stop-color="#1a3fa5"/><stop offset="1" stop-color="#0a8ad8"/></linearGradient></defs><path d="M0 0h152v62L76 46 0 62z" fill="#0a8ad8"/><path d="M4 0h144v54L76 40 4 54z" fill="url(#rb3)"/><circle cx="27" cy="21" r="13" stroke="#fff" stroke-width="2" fill="none"/><path d="M19 21l5-4 6 3 4-2M21 24l4 4" stroke="#fff" stroke-width="2" fill="none"/></svg>
    <span class="ribbon-label label-contact">Contact</span>
    <div class="contact-text">I am an Intellectual Property Lawyer and focus on patents, copyrights, trademarks, &amp; trade secrets. I work with small businesses and start ups in the chemical and biotech industries. I am small firm that can provide large-firm service at a reasonable price. I also can charge flat-fees for entrepreners in certain practice areas.</div>
  </article>
</section>

<footer class="site-footer">
  <div class="footer-map" role="img" aria-label="Grey world map illustration"></div>
  <nav class="footer-nav"><a href="#">Home</a><a href="#">About</a><a href="#">Practices</a><a href="#">People</a><a href="#">Blogs</a><a href="#">News</a><a href="#">Contact</a></nav>
  <p class="copyright">copyright@Velric Dunmore, PLLC all reserved.</p>
  <div class="footer-brand"><span class="brand-dot"></span>Velric Dunmore, PLLC</div>
</footer>
</body>
</html>
```